Brit Rock covers band "The Tin Kettles" requires poster for Marlowe Lounge Friday March 31st

I want a design for a poster (A3 and A4) and Facebook/Instagram ads.
Primary focus is the band name logo "The Tin Kettles", style as in attached file, followed by tag "Old Skool Brit Rock".
Backdrop to be 60's psychedelic art.
Secondary focus is the venue "The Marlowe Lounge"
Supporting text to include:
- 27 Fenwick Road, Chatswood SYDNEY
- Friday 31st March 2023
- 7:00 pm until late
- Bar sales refreshments
- NO admission fee

```html
<!DOCTYPE html>
<html lang="en">
<head>
<meta charset="utf-8">
<title>The Tin Kettles – Old Skool Brit Rock at The Marlowe Lounge</title>
<link rel="stylesheet" href="https://fonts.googleapis.com/css2?family=Exo+2:wght@600;700;800&family=Oswald:wght@600;700&display=swap">
<style>
  :root {
    --frame-grey: #a6a6a6;
    --panel-dark: #2b2b2b;
    --ink-dark: #262626;
    --paper-white: #f2f2f2;
    --band-grey: #9c9c9c;
    --venue-grey: #c4c4c4;
    --guitar-white: #ededed;
    --crowd-grey: #a9a9a9;
  }
  * { margin: 0; padding: 0; box-sizing: border-box; }
  html, body { width: 849px; height: 1200px; overflow: hidden; }
  body { background: var(--frame-grey); font-family: "Exo 2", Arial, sans-serif; }

  .poster { position: relative; width: 849px; height: 1200px; background: var(--frame-grey); overflow: hidden; }
  .stage { position: absolute; left: 25px; top: 24px; width: 798px; height: 1040px; background: var(--panel-dark); }

  .guitar-headstock {
    position: absolute; left: 507px; top: 112px; width: 300px; height: 630px;
    background: var(--guitar-white);
    border-radius: 70px 130px 40px 18px;
  }

  .tag { position: absolute; left: 77px; width: 417px; height: 74px; color: var(--ink-dark);
         font-weight: 700; font-size: 68px; line-height: 74px; text-align: center; }
  .tag--top { top: 213px; background: var(--paper-white); }
  .tag--bottom { top: 304px; background: var(--band-grey); }

  .band-name { position: absolute; left: 75px; top: 392px; width: 420px; color: var(--paper-white);
               font-family: "Oswald", "Arial Narrow", sans-serif;
               font-weight: 700; font-size: 128px; line-height: 124px; text-transform: uppercase; letter-spacing: 0; }
  .band-name span { display: block; white-space: nowrap; }

  .venue { position: absolute; left: 252px; top: 688px; color: var(--venue-grey);
           font-weight: 700; font-size: 24px; white-space: nowrap; }

  .details { position: absolute; left: 68px; top: 751px; width: 675px; height: 160px; background: var(--band-grey);
             display: flex; justify-content: space-between; padding: 26px 18px 0; }
  .detail { width: 128px; text-align: center; color: var(--ink-dark); }
  .detail svg { width: 60px; height: 60px; display: block; margin: 0 auto 18px; fill: none; stroke: var(--ink-dark); stroke-width: 2.4; stroke-linecap: round; stroke-linejoin: round; }
  .detail p { font-weight: 700; font-size: 15px; line-height: 24px; white-space: nowrap; }

  .crowd { position: absolute; left: 25px; top: 965px; width: 798px; height: 100px; background: var(--crowd-grey); }
</style>
</head>
<body>
<main class="poster">
  <div class="stage"></div>

  <div class="guitar-headstock" role="img" aria-label="Illustration of an electric guitar headstock with six tuning pegs"></div>

  <div class="tag tag--top">Old Skool</div>
  <div class="tag tag--bottom">Brit Rock</div>

  <h1 class="band-name"><span>The Tin</span><span>Kettles</span></h1>

  <p class="venue">”The Marlowe Lounge”</p>

  <section class="details">
    <div class="detail">
      <svg viewBox="0 0 60 60"><path d="M30 56 C18 40 14 32 14 24 a16 16 0 0 1 32 0 c0 8 -4 16 -16 32z"/><circle cx="30" cy="24" r="6"/></svg>
      <p>27 Fenwick Road,<br>Chatswood SYDNEY</p>
    </div>
    <div class="detail">
      <svg viewBox="0 0 60 60"><rect x="4" y="10" width="44" height="38" rx="3"/><line x1="4" y1="20" x2="48" y2="20"/><line x1="14" y1="6" x2="14" y2="14"/><line x1="38" y1="6" x2="38" y2="14"/><path d="M12 28h4M22 28h4M32 28h4M12 36h4M22 36h4"/><circle cx="46" cy="46" r="10"/><path d="M46 40v6h5"/></svg>
      <p>Friday 31st<br>March 2023</p>
    </div>
    <div class="detail">
      <svg viewBox="0 0 60 60"><circle cx="30" cy="30" r="26"/><circle cx="30" cy="30" r="21"/><path d="M30 15v15h-8"/></svg>
      <p>7:00 pm<br>until late</p>
    </div>
    <div class="detail">
      <svg viewBox="0 0 60 60"><path d="M36 4h8v10c4 3 6 7 6 12v30h-20v-30c0-5 2-9 6-12z"/><path d="M34 32h12v12h-12z"/><path d="M8 24h16c1 10-3 16-8 16s-9-6-8-16z"/><path d="M16 40v14M10 56h12"/></svg>
      <p>Bar sales<br>refreshments</p>
    </div>
    <div class="detail">
      <svg viewBox="0 0 60 60"><rect x="4" y="16" width="44" height="24" rx="2"/><rect x="8" y="20" width="36" height="16"/><circle cx="26" cy="28" r="4"/><path d="M50 20v24h-40M54 24v24h-40"/></svg>
      <p>NO<br>admission fee</p>
    </div>
  </section>

  <div class="crowd" role="img" aria-label="Silhouette of a cheering concert crowd with raised arms"></div>
</main>
</body>
</html>
```